Professional "Aviation Parts" Auction Website with Customer Login Backend Module

Need an "Aviation Parts" Website with 4 major listing options.
- AUCTION
Seller can list their items on the site as an auction with a small listing fee. Seller has to create an account in order to be able to create or edit a listing. Seller must be able to have a reserve price.
- SELLING
Sellers can list their items with a small listing fee. Imortant is, that Sellers has a back end module, (like lotvane) where they can log in and create or make changes to existing listings.
- BUYING
Buyers can search items either by part number in a search bar, or scroll through categories and subcategories to find the respective part.
- WANTED
Customers should be able to create a “Wanted” listing for items of interest.

In all four cases, customers (Buyers/Seller) must create an account to either place a bid, buy now, create a “wanted” listing or create/edit their own for sale/auction listing. NO login is required to search the website or browse through categories and to see listings. The website should be “Lotvane like” with login module, payment, coinrill connection, etc and easy to navigate. A design example is https://www.skylotra-hub.com/ . I’m open for all ideas.

Target Market(s)

Aviation Industry
Helicopter Industry

Industry/Entity Type

Aviation

Number of Pages Required

5+ page

Font styles to use
Serif
Sans Serif

Colors
85acd3
3176b5
9d9d9d
d3d3d3

Requirements
Must have
• Our company is called Torvinex.com, LLC and is specialized in aviation parts listings. The website must have 4 major options: Auction, Sell, Buy, and Wanted listings. The Buyer/Seller must create an account in order to bid, buy or sell an item. No login is required if someone just wants to browse the website to look for pricing and parts. Once they decide to purchase, they have to login or create an account. The same counts for the seller. Seller must create an account to list a "For Sale", "Auction" or "Wanted" Listing. Each listing requires a small listing fee, which will be charged by us and should be paid via CoinRill. CoinRill should be interfaced as a preferred payment method. Other payment options are available as well. The website idea is very similar to Lotvane. Same style listings as Lotvane and other auction pages. A good design idea is https://www.skylotra-hub.com/ to get a better understanding. The website must be easy to navigate and modern looking with a professional color scheme. The logo is attached. I would like to keep the website in a similar color scheme as the logo design.
• There should be two main Categories on the main page to select from:
• - Helicopter Listings
• - Airplane Listings
• The 1st "Sub-Category" once you click on either one of the top category, will be "Aircraft Make".
• The 2nd "Sub-Category" will be "Aircraft Model".
• The 3rd "Sub-Category" will be "Parts" for that specific aircraft.
• Also there should be a CoinRill interface, if a buyer wants to purchase an item, so they can use their credit card or request wire information from the seller after closing.
• It also has to include an option when a seller lists an item, they will be required to make a payment to us for listing on our website. For example $1.99 for a listing value up to $100. A listing fee for a sale value of up to $1,000 will be $4.99, and so on. Listing fee for up to $10,000 will be $14.99. Listing fee for up to $100.000 will be $49.99. This system is very similar to the Lotvane platform.
Nice to have
• It would be nice to have a easy to maintain back-end module which can easily be manged by our personnel.
Should not have
• The page should not look childish with random colors. A professional appearance and easy to navigate is a must.

```html
<!DOCTYPE html>
<html lang="en">
<head>
<meta charset="utf-8">
<title>Torvinex – Aviation Parts</title>
<link rel="stylesheet" href="https://fonts.googleapis.com/css2?family=Raleway:wght@400;500;600;700&family=Work+Sans:wght@400;500;600&display=swap">
<style>
:root{
  --blue:#3176b5;
  --blue-dark:#2a64a0;
  --blue-light:#85acd3;
  --grey:#9d9d9d;
  --grey-light:#d3d3d3;
  --ink:#222;
  --text:#555;
  --muted:#8a8a8a;
  --white:#fff;
  --footer:#d2d2d2;
}
*{box-sizing:border-box;margin:0;padding:0}
html,body{width:801px;height:1200px;overflow:hidden}
body{position:relative;background:var(--white);font-family:"Work Sans",sans-serif;color:var(--text)}
h1,h2,h3,h4{font-weight:400}
.abs{position:absolute}
/* header */
.brand{left:59px;top:37px;width:128px;text-align:center;font-family:"Raleway",sans-serif;font-size:19px;font-weight:500;letter-spacing:2px;color:var(--blue);line-height:22px}
.toplinks{left:385px;top:29px;font-size:9px;color:#444;white-space:nowrap}
.toplinks .sep{margin:0 10px}
.btn-account{left:638px;top:26px;width:106px;height:18px;background:var(--blue);color:var(--white);font-size:8.5px;font-weight:500;border-radius:2px;text-align:center;line-height:18px}
.nav{top:58px;font-family:"Raleway",sans-serif;font-size:8.5px;font-weight:600;letter-spacing:.6px;color:#555}
.cart{left:712px;top:57px;font-size:9px;color:#555;display:flex;align-items:center;gap:6px}
/* hero */
.hero{left:0;top:94px;width:801px;height:264px;background:linear-gradient(180deg,#5c6f80 0%,#3d4c46 45%,#2b3a31 100%)}
.hero-title{right:58px;top:168px;font-family:"Raleway",sans-serif;font-size:38px;font-weight:700;color:var(--white);letter-spacing:.5px}
.hero-sub{right:58px;top:216px;font-family:"Raleway",sans-serif;font-size:18px;font-weight:400;color:var(--white)}
.dots{left:768px;top:178px;display:flex;flex-direction:column;gap:3px}
.dots span{width:9px;height:9px;border:1.5px solid var(--white);border-radius:50%}
.dots span.on{background:var(--blue);border-color:var(--blue)}
/* search */
.tab{top:301px;height:29px;font-family:"Raleway",sans-serif;font-size:11.5px;font-weight:600;letter-spacing:.6px;text-align:center;line-height:29px}
.tab-heli{left:69px;width:138px;background:var(--blue);color:var(--white)}
.tab-plane{left:215px;width:125px;background:var(--white);color:#444;border:1px solid var(--grey-light)}
.search-panel{left:58px;top:317px;width:685px;height:71px;background:var(--white);box-shadow:0 2px 8px rgba(0,0,0,.15)}
.field{top:344px;height:29px;border:1px solid #bbb;border-radius:2px;font-size:10.5px;color:#666;padding-left:10px;line-height:27px}
.field .caret{position:absolute;right:8px;top:12px;border-left:3.5px solid transparent;border-right:3.5px solid transparent;border-top:4px solid #555}
.btn-search{left:617px;top:344px;width:116px;height:29px;background:var(--blue);color:var(--white);font-size:10.5px;padding-left:9px;line-height:29px;border-radius:2px}
.btn-search svg{position:absolute;right:10px;top:9px}
/* sections */
.sec-title{left:58px;font-family:"Raleway",sans-serif;font-size:17px;font-weight:700;letter-spacing:.6px;color:var(--blue)}
.rule{left:58px;width:685px;height:1px;background:var(--grey-light)}
.arrows{left:702px;display:flex;gap:3px}
.arrows span{width:19px;height:19px;border-radius:50%;background:#333;display:flex;align-items:center;justify-content:center}
.card{width:334px;height:140px;display:flex;background:var(--white);box-shadow:0 1px 5px rgba(0,0,0,.18)}
.card-media{width:125px;height:140px;flex:none}
.card-media.framed{border:1px solid #e2e2e2}
.card-body{padding:5px 11px 0;flex:1}
.card-title{font-size:11px;font-weight:600;color:var(--ink)}
.card-price{font-size:13.5px;color:#333;margin-top:6px}
.card-meta{display:flex;font-size:7.5px;color:#333;margin-top:6px}
.card-meta span:first-child{width:85px}
.card-desc{font-size:7.5px;line-height:14.5px;color:var(--muted);margin-top:7px}
.btn-buy{display:inline-block;margin-top:4px;background:var(--blue);color:var(--white);font-size:7px;font-weight:600;padding:0 7px;height:18px;line-height:18px;border-radius:1px}
/* footer */
.footer{left:0;top:929px;width:801px;height:271px;background:var(--footer)}
.f-head{font-size:9.5px;font-weight:400;color:#444}
.f-about-title{font-size:12px;font-weight:400;color:#444;letter-spacing:.3px}
.f-about{font-size:7.8px;line-height:14.6px;color:#555;width:200px}
.f-list{list-style:none;font-size:7.8px;color:#555}
.f-list li{height:19px;display:flex;align-items:center;gap:9px}
.f-list .chev{color:#666}
.f-list .ico{width:7px;height:7px;border-radius:50%;background:#555;display:inline-block}
.f-rule{left:58px;width:685px;height:1px;background:#c2c2c2}
.f-small{font-size:7.8px;color:#555}
.input-email{left:385px;top:1106px;width:226px;height:29px;border:1px solid #777;font-size:9px;color:#888;padding-left:14px;line-height:27px;background:var(--footer)}
.btn-subscribe{left:614px;top:1106px;width:122px;height:29px;background:var(--blue);color:var(--white);font-size:9px;font-weight:600;letter-spacing:.6px;text-align:center;line-height:29px}
.pay{top:1166px;display:flex;gap:8px;left:57px}
.pay span{width:29px;height:17px;background:var(--white);border-radius:1px}
.pay span.blue{background:#3b8fd6}
.copy{right:73px;top:1174px;font-size:7.8px;color:#555}
</style>
</head>
<body>

<header>
  <div class="abs brand">TORVINEX</div>
  <div class="abs toplinks">Help &amp; Contact: 0145 882 3306<span class="sep">|</span>Buyer/Seller Login</div>
  <div class="abs btn-account">Create Free Account</div>
  <nav>
    <span class="abs nav" style="left:275px">HOME</span>
    <span class="abs nav" style="left:340px">ONLINE CATALOG</span>
    <span class="abs nav" style="left:459px">WHO WE ARE</span>
    <span class="abs nav" style="left:558px">BLOG</span>
    <span class="abs nav" style="left:620px">CONTACT US</span>
    <span class="abs cart"><svg width="9" height="8" viewBox="0 0 9 8"><path d="M0 1h1.8l1.2 4.2h4.4L8.6 2H2.4" fill="none" stroke="#3176b5" stroke-width="1.3"/><circle cx="3.4" cy="7" r=".9" fill="#3176b5"/><circle cx="6.8" cy="7" r=".9" fill="#3176b5"/></svg>(0)</span>
  </nav>
</header>

<section class="abs hero" role="img" aria-label="Photo of a blue helicopter hovering in front of a forested mountain slope"></section>
<h1 class="abs hero-title">TORVINEX</h1>
<p class="abs hero-sub">Your One Stop Shop For Aviation Parts.</p>
<div class="abs dots"><span></span><span></span><span class="on"></span><span></span><span></span></div>

<div class="abs search-panel"></div>
<div class="abs tab tab-heli">HELICOPTER</div>
<div class="abs tab tab-plane">AIRPLANE</div>
<div class="abs field" style="left:69px;width:151px">Aircraft Make<span class="caret"></span></div>
<div class="abs field" style="left:226px;width:150px">Aircraft Model<span class="caret"></span></div>
<div class="abs field" style="left:383px;width:227px">Search by Part Number</div>
<div class="abs btn-search">Search<svg width="11" height="11" viewBox="0 0 11 11"><circle cx="4.5" cy="4.5" r="3.4" fill="none" stroke="#fff" stroke-width="1.6"/><path d="M7 7l3 3" stroke="#fff" stroke-width="1.8"/></svg></div>

<h2 class="abs sec-title" style="top:426px">RECENT LISTINGS</h2>
<div class="abs arrows" style="top:427px">
  <span><svg width="6" height="8" viewBox="0 0 6 8"><path d="M4.5 1L1.5 4l3 3" fill="none" stroke="#fff" stroke-width="1.5"/></svg></span>
  <span><svg width="6" height="8" viewBox="0 0 6 8"><path d="M1.5 1l3 3-3 3" fill="none" stroke="#fff" stroke-width="1.5"/></svg></span>
</div>
<div class="abs rule" style="top:455px"></div>

<article class="abs card" style="left:58px;top:480px">
  <div class="card-media" role="img" aria-label="Close-up photo of a jet engine fan" style="background:radial-gradient(circle at 40% 50%,#1d2f4a 0%,#6f8fb8 45%,#c6d3e2 100%)"></div>
  <div class="card-body">
    <h3 class="card-title">Product Title Goes Here</h3>
    <div class="card-price">$3,000</div>
    <div class="card-meta"><span>1 Bid</span><span>4d 2h left (Tue, 5PM)</span></div>
    <p class="card-desc">Sed ut perspiciatis unde omnis iste natus error sit voluptatem accusantium doloremque lau-dantium, totam rem aperiam,</p>
    <span class="btn-buy">BUY NOW</span>
  </div>
</article>
<article class="abs card" style="left:408px;top:480px">
  <div class="card-media framed" role="img" aria-label="Photo of a metal aircraft bracket part with red connectors" style="background:linear-gradient(135deg,#fff 30%,#c9c9c9 50%,#fff 70%)"></div>
  <div class="card-body">
    <h3 class="card-title">Product Title Goes Here</h3>
    <div class="card-price">$2,000</div>
    <div class="card-meta"><span>3 Bid</span><span>2d 6h left (Wed, 8AM)</span></div>
    <p class="card-desc">Sed ut perspiciatis unde omnis iste natus error sit voluptatem accusantium doloremque lau-dantium, totam rem aperiam,</p>
    <span class="btn-buy">BUY NOW</span>
  </div>
</article>

<h2 class="abs sec-title" style="top:670px">FEATURED LISTINGS</h2>
<div class="abs arrows" style="top:671px">
  <span><svg width="6" height="8" viewBox="0 0 6 8"><path d="M4.5 1L1.5 4l3 3" fill="none" stroke="#fff" stroke-width="1.5"/></svg></span>
  <span><svg width="6" height="8" viewBox="0 0 6 8"><path d="M1.5 1l3 3-3 3" fill="none" stroke="#fff" stroke-width="1.5"/></svg></span>
</div>
<div class="abs rule" style="top:699px"></div>

<article class="abs card" style="left:58px;top:723px">
  <div class="card-media" role="img" aria-label="Photo of a helicopter rotor head against blue sky" style="background:linear-gradient(180deg,#3f7fd8 0%,#5b8fd6 45%,#6d7378 75%,#9a9ea2 100%)"></div>
  <div class="card-body">
    <h3 class="card-title">Product Title Goes Here</h3>
    <div class="card-price">$4,000</div>
    <div class="card-meta"><span>6 Bid</span><span>1d 2h left (Tue, 5PM)</span></div>
    <p class="card-desc">Sed ut perspiciatis unde omnis iste natus error sit voluptatem accusantium doloremque lau-dantium, totam rem aperiam,</p>
    <span class="btn-buy">BUY NOW</span>
  </div>
</article>
<article class="abs card" style="left:408px;top:723px">
  <div class="card-media framed" role="img" aria-label="Photo of a turbine engine assembly" style="background:radial-gradient(ellipse at 50% 50%,#9a9a9a 0%,#d5d5d5 35%,#fff 60%)"></div>
  <div class="card-body">
    <h3 class="card-title">Product Title Goes Here</h3>
    <div class="card-price">$5,000</div>
    <div class="card-meta"><span>8 Bid</span><span>8d 9h left (Wed, 8AM)</span></div>
    <p class="card-desc">Sed ut perspiciatis unde omnis iste natus error sit voluptatem accusantium doloremque lau-dantium, totam rem aperiam,</p>
    <span class="btn-buy">BUY NOW</span>
  </div>
</article>

<footer class="abs footer"></footer>
<h4 class="abs f-about-title" style="left:58px;top:957px">About Torvinex</h4>
<p class="abs f-about" style="left:58px;top:984px">Lorem Ipsum is simply dummy text of the print-ing and typesetting industry. Lorem Ipsum has been the industry's standard dummy text ever since the 1500s, when an unknown printer took a galley of type and scrambled</p>

<h4 class="abs f-head" style="left:353px;top:962px">Help</h4>
<ul class="abs f-list" style="left:348px;top:980px">
  <li><span class="chev">&gt;</span>FAQ</li>
  <li><span class="chev">&gt;</span>Shipping &amp; Returns</li>
  <li><span class="chev">&gt;</span>Store Policy</li>
  <li><span class="chev">&gt;</span>Payment Methods</li>
</ul>

<h4 class="abs f-head" style="left:537px;top:962px">Company</h4>
<ul class="abs f-list" style="left:532px;top:980px">
  <li style="height:16.5px"><span class="chev">&gt;</span>Shop</li>
  <li style="height:16.5px"><span class="chev">&gt;</span>Extras</li>
  <li style="height:16.5px"><span class="chev">&gt;</span>About</li>
  <li style="height:16.5px"><span class="chev">&gt;</span>Blog</li>
  <li style="height:16.5px"><span class="chev">&gt;</span>Contact</li>
</ul>

<h4 class="abs f-head" style="left:682px;top:962px">Follow Us</h4>
<ul class="abs f-list" style="left:677px;top:980px">
  <li><span class="ico"></span>Friendwall</li>
  <li><span class="ico"></span>Snapgrid</li>
  <li><span class="ico"></span>Careerlink</li>
  <li><span class="ico"></span>Chirper</li>
</ul>

<div class="abs f-rule" style="top:1090px"></div>
<p class="abs f-small" style="left:70px;top:1108px">Visit Our Stores</p>
<p class="abs f-small" style="left:70px;top:1127px;display:flex;align-items:center;gap:3px"><svg width="7" height="7" viewBox="0 0 7 7"><path d="M1.3 0.3l1.3 1.5-.7.9c.4.9 1 1.5 1.9 1.9l.9-.7 1.5 1.3-.8 1.1C2.8 6 1 4.2.2 1.1z" fill="#444"/></svg>Customer service: 145-882-3306</p>
<div class="abs input-email">Your Email Address</div>
<div class="abs btn-subscribe">SUBSCRIBE</div>
<div class="abs f-rule" style="top:1151px"></div>

<div class="abs pay" aria-label="Accepted payment methods">
  <span></span><span></span><span></span><span></span><span></span><span class="blue"></span>
</div>
<p class="abs copy">@2018 All rights reserved to Torvinex.</p>

</body>
</html>
```